Web design for a Senior Home Care company

I want a web design for a home care company called Willowmere Home Care. What WHC does is send caregivers into people's homes to assist with daily living needs such as companionship, food preparation, cleaning, bathing, using the bathroom, etc. Most of the clients are seniors. The people deciding to use WHC are usually the 50 year old children of these senior citizens. Most visitors to the site will be women searching for this service for their parents.

The call to action is to inspire the website visitors to call us to set up an appointment to meet them in their home. The site design should inspire confidence in Willowmere Home Care to care for people's needs. We want to show the same attributes that a parent should have. Safety, Security and Loving Care.

Again, the goal of the site is to inspire and make it EASY for visitors to contact us either by phone call or through the website. The first choice is that they call us.

To help you with your ideas, In the attachments I've included different versions of our logo, a site map, examples of photos we might use and very rough draft of the website copy.

Target Market(s)

The customers will mostly be seniors. But, the people who will decide to use the company will the the 50 year old children of those seniors. Also, it is mostly women who are looking for help for their parents.

Industry/Entity Type

It Company

Number of Pages Required

5+ page

Requirements
Nice to have
• I want site visitors to easily be able to contact us with a phone call or through the website. The home page should inspire people to call us.

```html
<!DOCTYPE html>
<html lang="en">
<head>
<meta charset="utf-8">
<title>Willowmere Home Care</title>
<link href="https://fonts.googleapis.com/css2?family=Raleway:wght@400;500;600&display=swap" rel="stylesheet">
<style>
:root{
  --blue:#4a6db3;
  --blue-dark:#3a5aa3;
  --blue-light:#6a8fd6;
  --heading:#3f65ad;
  --text:#444;
  --muted:#6b6b6b;
  --link:#2f7fc9;
  --white:#fff;
  --line:#dcdcdc;
}
*{box-sizing:border-box;margin:0;padding:0}
html,body{width:1200px;height:2273px;overflow:hidden;background:var(--white);font-family:'Raleway',sans-serif;color:var(--text)}
.page{position:relative;width:1200px;height:2273px}

/* header */
.site-header{position:absolute;top:0;left:0;width:1200px;height:86px;border-top:3px solid var(--blue);background:var(--white)}
.brand{position:absolute;left:98px;top:16px;display:flex;align-items:center;gap:10px}
.brand-mark{width:44px;height:44px;border:3px solid var(--blue);border-radius:4px}
.brand-name{color:var(--blue);font-weight:600;font-size:26px;line-height:1;letter-spacing:1px;text-transform:uppercase}
.brand-name small{font-size:17px;letter-spacing:3px}
.main-nav{position:absolute;top:38px;right:100px;display:flex;gap:36px;font-size:13px;color:#333}

/* hero */
.hero{position:absolute;top:86px;left:0;width:1200px;height:428px;background:linear-gradient(90deg,#7c7c7c 0%,#a7a7a7 35%,#cfc6c0 60%,#b9a9a0 100%)}
.hero-brand{position:absolute;left:80px;top:60px;display:flex;align-items:center;gap:16px;color:var(--white);font-weight:600;font-size:46px;letter-spacing:2px;text-transform:uppercase;line-height:1}
.hero-brand .brand-mark{width:74px;height:74px;border-color:var(--white)}
.hero-brand small{font-size:29px;letter-spacing:5px}
.hero-title{position:absolute;left:97px;top:190px;color:var(--white);font-size:34px;font-weight:600}
.hero-sub{position:absolute;left:97px;top:243px;color:var(--white);font-size:25px;font-weight:400}
.hero-phone{position:absolute;left:97px;top:287px;color:var(--white);font-size:24px;font-weight:500}
.arrow{position:absolute;width:24px;height:40px}

/* booking */
.booking{position:absolute;left:99px;top:460px;width:1001px;height:95px;background:linear-gradient(180deg,var(--blue-light),var(--blue));box-shadow:0 14px 18px -10px rgba(0,0,0,.35);display:flex;align-items:center;padding:0 43px;gap:28px}
.booking .field{width:160px;height:40px;background:var(--white);border-radius:2px;font-size:13px;color:#aaa;padding:12px 12px}
.booking .book-btn{margin-left:8px;width:158px;height:40px;border:1px solid #a9c2ef;background:var(--blue-light);color:var(--white);font-size:15px;font-weight:600;display:flex;align-items:center;justify-content:center;border-radius:2px}

/* about */
.about{position:absolute;top:555px;left:0;width:1200px;height:349px;text-align:center}
.section-title{color:var(--heading);font-size:25px;font-weight:600}
.about .section-title{margin-top:50px}
.about p{width:940px;margin:22px auto 0;font-size:12.2px;line-height:31px;color:#555}
.btn-row{margin-top:30px;display:flex;justify-content:center;gap:21px}
.btn{height:39px;display:flex;align-items:center;justify-content:center;color:var(--white);font-size:15px;border-radius:3px}
.btn-primary{width:151px;background:linear-gradient(180deg,#4d6fbf,#2f4f99)}
.btn-dark{width:133px;background:linear-gradient(180deg,#777,#4a4a4a)}

/* services */
.services{position:absolute;top:904px;left:0;width:1200px;height:437px;background:linear-gradient(135deg,#5377c2,#4265b0 50%,#3e62ad);text-align:center;color:var(--white)}
.services .section-title{color:var(--white);margin-top:45px}
.services p{width:900px;margin:20px auto 0;font-size:14px;line-height:30px}
.service-list{position:absolute;left:99px;top:197px;display:flex;gap:10px}
.service{width:244px}
.service .photo{width:244px;height:147px}
.service h3{margin-top:25px;font-size:21px;font-weight:600}

/* testimonials */
.testimonials{position:absolute;top:1341px;left:0;width:1200px;height:317px}
.testimonials .section-title{position:absolute;left:97px;top:38px;font-size:25px}
.view-all{position:absolute;right:100px;top:62px;font-size:11px;color:var(--link)}
.rule{position:absolute;left:97px;top:86px;width:1003px;height:1px;background:var(--line)}
.quote-mark{position:absolute;left:99px;top:110px;width:24px;height:20px}
.quote-text{position:absolute;left:123px;top:144px;width:668px;font-size:11.8px;line-height:26px;color:#444}
.quote-by{position:absolute;left:123px;top:240px;font-size:13px;line-height:21px;color:var(--link)}
.avatars{position:absolute;left:818px;top:122px}

/* how it works */
.how{position:absolute;top:1658px;left:0;width:1200px;height:362px;background:linear-gradient(90deg,#e4ebe8 0%,#dfe6e3 45%,#c9b3a3 60%,#a98c78 100%)}
.how .section-title{position:absolute;left:95px;top:43px;font-size:25px}
.how p{position:absolute;left:95px;top:95px;width:500px;font-size:12.4px;line-height:31.5px;color:#333}
.btn-outline{position:absolute;left:97px;top:272px;width:154px;height:35px;border:1px solid #aab;display:flex;align-items:center;justify-content:center;font-size:15px;color:#333;background:rgba(255,255,255,.25)}

/* footer */
.site-footer{position:absolute;top:2020px;left:0;width:1200px;height:253px;background:linear-gradient(180deg,#5a7fc7,#3a58a3);color:var(--white);text-align:center}
.social{position:absolute;left:460px;top:42px;display:flex;gap:24px}
.social-link{width:56px;height:56px;border:3px solid var(--white);border-radius:50%;display:flex;align-items:center;justify-content:center;font-size:11px;font-weight:600;color:var(--white)}
.footer-rule{position:absolute;left:485px;top:129px;width:233px;height:2px;background:rgba(255,255,255,.3)}
.footer-nav{position:absolute;left:0;top:161px;width:1200px;display:flex;justify-content:center;gap:28px;font-size:13px;align-items:center}
.footer-nav .dot{width:4px;height:4px;border-radius:50%;background:rgba(255,255,255,.7)}
.footer-nav .home{font-size:15px}
.copyright{position:absolute;left:0;top:204px;width:1200px;font-size:12px}
</style>
</head>
<body>
<div class="page">

  <header class="site-header">
    <div class="brand"><span class="brand-mark"></span><span class="brand-name">Willowmere<br><small>Home Care</small></span></div>
    <nav class="main-nav">
      <span>About Us</span><span>Services</span><span>Free In-Home Consultation</span><span>Contact Us</span><span>News</span><span>Client Portal</span>
    </nav>
  </header>

  <section class="hero" role="img" aria-label="Photo of a smiling senior woman playing cards with a young caregiver">
    <div class="hero-brand"><span class="brand-mark"></span><span>Willowmere<br><small>Home Care</small></span></div>
    <h1 class="hero-title">Willowmere Home Care</h1>
    <div class="hero-sub">Family-Owned, Service You Can Trust</div>
    <div class="hero-phone">( +1 ) 555 014 2290</div>
    <svg class="arrow" style="left:36px;top:192px" viewBox="0 0 24 40"><polyline points="20,2 4,20 20,38" fill="none" stroke="#fff" stroke-width="2"/></svg>
    <svg class="arrow" style="left:1146px;top:192px" viewBox="0 0 24 40"><polyline points="4,2 20,20 4,38" fill="none" stroke="#fff" stroke-width="2"/></svg>
  </section>

  <form class="booking">
    <div class="field">Name</div>
    <div class="field">Email</div>
    <div class="field">Date</div>
    <div class="field">Address</div>
    <div class="book-btn">Book Appoinment</div>
  </form>

  <section class="about">
    <h2 class="section-title">About Our Willowmere Homecare</h2>
    <p>Willowmere Home Care is a local family owned and operated agency devoted to helping families like yours in the Cedar Valley.  We take pride in the relationships we develop with our clients. We understand this is a challenging time and we are dedicated to providing the peace of mind you deserve. At Willowmere Home Care we do more than just watch your loved ones. We care for them with programs designed to keep them both mentally and physically comfortable, happy and healthy. Being a family agency is what makes Willowmere Home Care special and sets us apart. We treat our caregivers as part of the family too. They</p>
    <div class="btn-row"><span class="btn btn-primary">View more info</span><span class="btn btn-dark">Quick Contact</span></div>
  </section>

  <section class="services">
    <h2 class="section-title">Services We Do</h2>
    <p>Willowmere Home Care offers a wide variety of home care services, from once a week visits to 24-hour care. Since every situation is unique, we work together with you to create the perfect program. Here is just a short list of the services we provide.</p>
    <svg class="arrow" style="left:40px;top:255px" viewBox="0 0 24 40"><polyline points="18,6 6,20 18,34" fill="none" stroke="#fff" stroke-width="2"/></svg>
    <svg class="arrow" style="left:1140px;top:255px" viewBox="0 0 24 40"><polyline points="6,6 18,20 6,34" fill="none" stroke="#fff" stroke-width="2"/></svg>
    <div class="service-list">
      <div class="service"><div class="photo" role="img" aria-label="Photo of a caregiver sitting with an elderly man" style="background:linear-gradient(135deg,#e9e4e6,#9a7f86)"></div><h3>Companionship</h3></div>
      <div class="service"><div class="photo" role="img" aria-label="Photo of a caregiver helping a senior prepare food" style="background:linear-gradient(135deg,#b79a78,#6e5a48)"></div><h3>Food Preparation</h3></div>
      <div class="service"><div class="photo" role="img" aria-label="Photo of a senior woman and caregiver outdoors among flowers" style="background:linear-gradient(135deg,#d9b44a,#5f8a4a)"></div><h3>Cleaning</h3></div>
      <div class="service"><div class="photo" role="img" aria-label="Photo of a caregiver helping a senior woman on the stairs" style="background:linear-gradient(135deg,#cfc8be,#4e8fb3)"></div><h3>Bathing</h3></div>
    </div>
  </section>

  <section class="testimonials">
    <h2 class="section-title">Client's Testimonial</h2>
    <span class="view-all">View All &gt;&gt;</span>
    <div class="rule"></div>
    <svg class="quote-mark" viewBox="0 0 24 20"><path d="M0 10 Q0 2 8 0 L9 3 Q5 5 5 9 L10 9 L10 20 L0 20 Z M13 10 Q13 2 21 0 L22 3 Q18 5 18 9 L23 9 L23 20 L13 20 Z" fill="#444"/></svg>
    <p class="quote-text">Per et expetenda comprehensam, mei scripta accusata adolescens cu. Soluta adipisci eam ut. Ei zril impetus eum, patrio-<br>que euripidis vel ea, cu nec tempor feugiat. Vim elit saepe utroque in, ipsum dolore voluptua ex quo. Ea erat vidit inermis<br>per, tollit semper offendit an eos Ea eam augue graecis perpetua, pri ea oportere dissentiet,</p>
    <div class="quote-by">By<br>Quietbrook - LMV</div>
    <svg class="avatars" width="280" height="165" viewBox="0 0 280 165" role="img" aria-label="Client portrait thumbnails">
      <defs><linearGradient id="av" x1="0" y1="0" x2="0" y2="1"><stop offset="0" stop-color="#d9dde3"/><stop offset="1" stop-color="#8a8f98"/></linearGradient></defs>
      <polygon points="42,0 78,20 78,60 42,80 6,60 6,20" fill="url(#av)" stroke="#aaa" stroke-width="2"/>
      <polygon points="137,0 173,20 173,60 137,80 101,60 101,20" fill="url(#av)" stroke="#aaa" stroke-width="2"/>
      <polygon points="232,0 268,20 268,60 232,80 196,60 196,20" fill="url(#av)" stroke="#ddd" stroke-width="2"/>
      <polygon points="90,77 126,97 126,137 90,157 54,137 54,97" fill="url(#av)" stroke="#4a3f9c" stroke-width="3"/>
      <polygon points="185,77 221,97 221,137 185,157 149,137 149,97" fill="url(#av)" stroke="#ddd" stroke-width="2"/>
    </svg>
  </section>

  <section class="how" role="img" aria-label="Photo of a young hand gently holding an elderly hand">
    <h2 class="section-title">How It Works</h2>
    <p>Willowmere Home Care is always seeking enthusiastic caregivers to join our growing team. If you are a professional or looking to start out, we'd love to hear from you. We are family-owned and pride ourselves in getting to know and working closely with our staff. We offer competitive pay and benefits. We take pride in providing good and-long-term jobs for our team.</p>
    <span class="btn-outline">Read More Info</span>
  </section>

  <footer class="site-footer">
    <nav class="social">
      <span class="social-link">Kinfo</span>
      <span class="social-link">Chirp</span>
      <span class="social-link">Feedr</span>
      <span class="social-link">Circa</span>
    </nav>
    <div class="footer-rule"></div>
    <nav class="footer-nav">
      <span class="home">Home</span><i class="dot"></i><span>About Us</span><i class="dot"></i><span>Services</span><i class="dot"></i><span>News &amp; Events</span><i class="dot"></i><span>Contact Us</span><i class="dot"></i><span>Publications</span>
    </nav>
    <div class="copyright">All Rights Reserved . copyrights2016@willowmerecare.com</div>
  </footer>

</div>
</body>
</html>
```